TrueLane Collision Repair Web Site

Create a web site that will inform my potential customers about the services I provide. We are a Automotive Collision repair business that uses the latest state of the art equipment, computerized paint matching highly trained technicians, have over 30 years experience. We work with all all insurance programs. Our Moto is "Fixed Right, The First Time, Every Time". TrueLane, The intelligent choice in collision repair.

Target Market(s)

People that have been in a auto collision, needs windshield replaced, people that drive 10 year or newer cars

Industry/Entity Type

Automotive

Coding

Coded - Design and coding required

Number of Pages Required

4 page

Font styles to use
Sans Serif

Requirements
Must have
• Logo, Place for Phone number, I need to be able to put the code in so I can use a tracking phone number
• site needs to be mobile ready or adaptive
• May want to have a photo of a high end car
• here is a web site for example with the pages that I want
• https://www.brisvaleautobody.example/online-repair-estimate,
• https://www.brisvaleautobody.example/schedule-appointment
• https://www.brisvaleautobody.example/collision-repair/auto-body-repair
• https://www.brisvaleautobody.example/contact
Nice to have
• Be great if the Car in the log could have the front damaged then have it fix in a animation. Not sure if could be done here

```html
<!DOCTYPE html>
<html lang="en">
<head>
<meta charset="utf-8">
<title>TrueLane Collision Repair – About Us</title>
<link href="https://fonts.googleapis.com/css2?family=Open+Sans:wght@400;600;700&family=Ubuntu:wght@400;500;700&display=swap" rel="stylesheet">
<style>
:root{
  --blue:#1b56a6;
  --blue-bar:#2e71c1;
  --red:#f04a4f;
  --side:#e3ebf5;
  --text:#7a7a7a;
  --ink:#222;
  --footer:#212022;
  --footer-bottom:#171717;
  --line:#dfe5ee;
}
*{box-sizing:border-box;margin:0;padding:0}
html,body{width:1145px;height:1200px;overflow:hidden;background:#fff}
body{position:relative;font-family:"Open Sans",sans-serif;color:var(--text)}
.abs{position:absolute}
ul{list-style:none}

/* top bar */
.top-bar{left:0;top:0;width:1145px;height:20px;background:var(--blue-bar)}
.top-bar .appt{left:224px;top:4px;color:#fff;font:700 8.6px "Open Sans",sans-serif;display:flex;align-items:center;gap:6px}
.top-bar .social{right:222px;top:5px;display:flex;gap:5px}
.top-bar .social span{width:10px;height:10px;background:#fff;border-radius:1px}

/* header */
.header-line{left:0;top:87px;width:1145px;height:2px;background:var(--blue)}
.brand{left:224px;top:30px;color:var(--blue);font-family:"Ubuntu",sans-serif;font-weight:500;display:flex;align-items:center;gap:7px}
.brand .dot{width:14px;height:14px;border-radius:50%;background:var(--blue)}
.brand .name{font-size:24px;line-height:24px}
.brand .sub{font-size:10.5px;letter-spacing:.6px;line-height:14px}
.main-nav{left:446px;top:48px;display:flex;gap:10px;font:500 8.6px "Open Sans",sans-serif;color:var(--blue)}
.call{left:821px;top:39px}
.call .label{font:700 7.6px "Open Sans",sans-serif;color:var(--ink)}
.call .num{font:600 18.5px "Open Sans",sans-serif;color:var(--red);margin-top:2px;letter-spacing:.3px}

.crumb{left:224px;top:103px;font-size:8.8px;color:var(--ink)}
.crumb a{color:var(--blue);text-decoration:none}

/* main panel */
.panel{left:223px;top:125px;width:700px;height:525px;background:var(--side)}
.side-nav{left:236px;top:141px}
.side-nav li{height:25px;display:flex;align-items:center;gap:6px;font:400 9.5px "Open Sans",sans-serif;color:var(--blue)}
.side-nav svg{width:12px;height:12px;fill:var(--blue)}
.content{left:442px;top:128px;width:477px;height:516px;background:#fff}
.section-title{position:absolute;font:700 15px/18px "Ubuntu",sans-serif;color:var(--blue);margin:0}
.intro{left:452px;top:160px;width:455px;font-size:8.3px;line-height:11.5px}
.services{left:457px;top:236px;font-size:8.5px}
.services li{height:15px;display:flex;align-items:center;gap:7px}
.services li::before{content:"";width:3px;height:3px;background:var(--red)}

.faq{left:451px;width:460px;border:1px solid var(--line);background:#fff}
.faq .q{position:absolute;left:7px;right:34px;font:500 9px/10.6px "Ubuntu",sans-serif;color:var(--blue);padding-left:12px;text-indent:-12px}
.faq .toggle{position:absolute;right:7px;width:8px;height:8px}
.faq .answer{position:absolute;left:9px;top:25px;right:30px;font-size:8.3px;line-height:15px;border-top:1px solid var(--line);padding-top:3px}

/* brands */
.brands-title{left:0;top:686px;width:1145px;text-align:center;font:700 22px "Open Sans",sans-serif;color:var(--ink);letter-spacing:.2px}
.brands-rule{left:546px;width:53px;height:1px;background:var(--blue-bar)}
.partner{top:758px;width:84px;height:65px;border:1px solid #e6e6e6;display:flex;align-items:center;justify-content:center}
.partner span{width:48px;height:34px;background:#dadada;border-radius:6px}
.partner span.round{width:40px;height:40px;border-radius:50%}
.arrow-btn{top:782px;width:21px;height:21px;border:1px solid #ddd;border-radius:50%;display:flex;align-items:center;justify-content:center}

/* footer */
.zigzag{left:0;top:855px}
.footer{left:0;top:861px;width:1145px;height:295px;background:var(--footer)}
.f-title{font:700 9.6px "Open Sans",sans-serif;color:#fff}
.news-input{left:221px;top:912px;width:149px;height:23px;background:#111;color:#8a8a8a;font-size:7px;padding:7px 12px;letter-spacing:.3px}
.news-btn{left:370px;top:912px;width:66px;height:23px;background:var(--red);color:#fff;font:700 6.8px "Open Sans",sans-serif;text-align:center;line-height:23px;letter-spacing:.3px}
.areas{left:514px;top:886px;font:700 16px/18.5px "Ubuntu",sans-serif;color:#fff;letter-spacing:.4px}
.hours{left:775px;top:886px;color:#fff}
.hours .label{font:700 9.6px "Open Sans",sans-serif}
.hours .num{font:700 30px "Open Sans",sans-serif;line-height:34px;letter-spacing:.5px}
.f-divider{left:223px;top:962px;width:700px;height:1px;background:#444}
.f-col{top:983px}
.f-col h3{font:700 9.3px "Open Sans",sans-serif;color:#fff;margin-bottom:7px}
.f-col li{font-size:8px;color:#e6e6e6;height:12.5px;display:flex;align-items:center;gap:7px}
.f-col li::before{content:"";border-left:3px solid #777;border-top:2px solid transparent;border-bottom:2px solid transparent}
.bottom{left:0;top:1156px;width:1145px;height:44px;background:var(--footer-bottom)}
.copy{left:224px;top:1169px;font-size:7.6px;color:#ddd}
.cards{left:565px;top:1170px;display:flex;gap:3px}
.cards span{width:22px;height:10px;background:#e8e8e8;border-radius:1px}
.socials{left:781px;top:1162px;display:flex;gap:7px}
.socials span{width:20px;height:20px;border-radius:50%;background:#3a3a3a}
</style>
</head>
<body>

<!-- top bar -->
<div class="abs top-bar">
  <div class="abs appt">
    <svg width="13" height="9" viewBox="0 0 13 9"><rect x=".6" y=".6" width="11.8" height="7.8" fill="none" stroke="#fff" stroke-width="1.2"/><path d="M.6.6 6.5 5 12.4.6" fill="none" stroke="#fff" stroke-width="1.2"/></svg>
    GET AN APPOINTMENT
  </div>
  <div class="abs social"><span></span><span></span><span></span></div>
</div>

<!-- header -->
<div class="abs brand">
  <span class="dot"></span>
  <div><div class="name">TrueLane</div><div class="sub">Collision Repair</div></div>
</div>
<nav class="abs main-nav">
  <span>LOCATIONS</span><span>|</span>
  <span>AUTO GLASS</span><span>|</span>
  <span>COLLISION REPAIR</span><span>|</span>
  <span>EMPLOYMENT</span><span>|</span>
  <span>CONTACT</span>
</nav>
<div class="abs call">
  <div class="label">CALL US NOW:</div>
  <div class="num">+ 1111 1111</div>
</div>
<div class="abs header-line"></div>

<div class="abs crumb">HOME | <a href="#">ABOUT US</a></div>

<!-- main panel -->
<div class="abs panel"></div>
<ul class="abs side-nav">
  <li><svg viewBox="0 0 12 12"><circle cx="5" cy="5" r="3.6" fill="none" stroke="#1b56a6" stroke-width="1.3"/><path d="M7.6 7.6 11 11" stroke="#1b56a6" stroke-width="1.5"/></svg>Find Location</li>
  <li><svg viewBox="0 0 12 12"><rect x="1" y="2" width="10" height="9" fill="none" stroke="#1b56a6" stroke-width="1.2"/><rect x="1" y="2" width="10" height="2.5"/><rect x="3" y="6" width="1.5" height="1.5"/><rect x="6" y="6" width="1.5" height="1.5"/><rect x="3" y="8.5" width="1.5" height="1.5"/></svg>Schedule Appointement</li>
  <li><svg viewBox="0 0 12 12"><rect x="2" y="1" width="8" height="10" fill="none" stroke="#1b56a6" stroke-width="1.2"/><path d="M4 4h4M4 6h4M4 8h3" stroke="#1b56a6"/></svg>Instant Auto Glass Qoute</li>
  <li><svg viewBox="0 0 12 12"><rect x="1" y="3" width="8" height="8" fill="none" stroke="#1b56a6" stroke-width="1.2"/><path d="M3 6h4M3 8h3" stroke="#1b56a6"/><path d="M7 6 11 1.5" stroke="#1b56a6" stroke-width="1.4"/></svg>Online Collision Estimate</li>
  <li><svg viewBox="0 0 12 12"><circle cx="6" cy="4" r="2.8"/><path d="M1 12c0-4 2.5-5 5-5s5 1 5 5z"/></svg>Customer Care</li>
  <li><svg viewBox="0 0 12 12"><circle cx="6" cy="3.5" r="2.8"/><path d="M1 11c0-3.5 2.5-4.5 5-4.5s5 1 5 4.5z"/></svg>Employment</li>
  <li><svg viewBox="0 0 12 12"><path d="M1 6 11 1 8 11 6 7z"/></svg>Feedback</li>
</ul>

<div class="abs content"></div>
<h2 class="section-title" style="left:454px;top:138px">About Us</h2>
<h2 class="section-title" style="left:454px;top:213px">Services</h2>
<h2 class="section-title" style="left:452px;top:298px">FAQ</h2>
<p class="abs intro">We are a family owned and operated business that takes pride in delivering a product we can be proud of. The TrueLane Collision Repair center is a state of the art collision repair facility that guarantee the highest quality repair and complete customer satisfaction.</p>
<ul class="abs services">
  <li>Collision Repair</li>
  <li>Frame Repair</li>
  <li>Alignment</li>
</ul>

<div class="abs faq" style="top:323px;height:81px">
  <div class="q" style="top:6px">Q: I have an insurance estimate already do I need to get more estimates?</div>
  <svg class="toggle" style="top:10px" viewBox="0 0 8 8"><rect y="3" width="8" height="2" fill="#1b56a6"/></svg>
  <p class="answer">No, we will work with the estimate the insurance company provided to you.&nbsp;&nbsp; If we discover any additional damage when we disassemble and blueprint your vehicle we will contact your insurance company and inform them of the additional damages and in most cases bill the insurance company directly.</p>
</div>
<div class="abs faq" style="top:415px;height:23px">
  <div class="q" style="top:5px">Q: Can you see all the damage during the estimate?</div>
  <svg class="toggle" style="top:8px" viewBox="0 0 8 8"><path d="M3 0h2v8H3zM0 3h8v2H0z" fill="#1b56a6"/></svg>
</div>
<div class="abs faq" style="top:448px;height:34px">
  <div class="q" style="top:5px">Q: I got in an accident and the person that hit me wants to pay to repair my car without<br>filing an insurance claim. Is this a good Idea?</div>
  <svg class="toggle" style="top:8px" viewBox="0 0 8 8"><path d="M3 0h2v8H3zM0 3h8v2H0z" fill="#1b56a6"/></svg>
</div>
<div class="abs faq" style="top:493px;height:34px">
  <div class="q" style="top:5px">Q: My final bill was greater than the estimate. Why can't you write an estimate that will include everything that my car will need for repairs?</div>
  <svg class="toggle" style="top:8px" viewBox="0 0 8 8"><path d="M3 0h2v8H3zM0 3h8v2H0z" fill="#1b56a6"/></svg>
</div>
<div class="abs faq" style="top:539px;height:34px">
  <div class="q" style="top:5px">Q: Why will you have to blend paint into the panels adjacent to the repairs that need to be done on my vehicle?</div>
  <svg class="toggle" style="top:8px" viewBox="0 0 8 8"><path d="M3 0h2v8H3zM0 3h8v2H0z" fill="#1b56a6"/></svg>
</div>
<div class="abs faq" style="top:584px;height:24px">
  <div class="q" style="top:5px">Q: Why doesn’t the paint on my bumper match the paint on the rest of my vehicle?</div>
  <svg class="toggle" style="top:8px" viewBox="0 0 8 8"><path d="M3 0h2v8H3zM0 3h8v2H0z" fill="#1b56a6"/></svg>
</div>

<!-- brands & partners -->
<h2 class="abs brands-title">BRANDS &amp; PARTNERS</h2>
<div class="abs brands-rule" style="top:722px"></div>
<div class="abs brands-rule" style="top:725px"></div>
<div class="abs arrow-btn" style="left:233px"><svg width="6" height="8" viewBox="0 0 6 8"><path d="M4.5 1 1.5 4l3 3" fill="none" stroke="#555" stroke-width="1.1"/></svg></div>
<div class="abs arrow-btn" style="left:891px"><svg width="6" height="8" viewBox="0 0 6 8"><path d="M1.5 1l3 3-3 3" fill="none" stroke="#555" stroke-width="1.1"/></svg></div>
<div class="abs partner" style="left:275px" role="img" aria-label="Partner badge"><span></span></div>
<div class="abs partner" style="left:377px" role="img" aria-label="Partner badge"><span></span></div>
<div class="abs partner" style="left:480px" role="img" aria-label="Partner badge"><span class="round"></span></div>
<div class="abs partner" style="left:582px" role="img" aria-label="Partner badge"><span></span></div>
<div class="abs partner" style="left:685px" role="img" aria-label="Partner badge"><span class="round"></span></div>
<div class="abs partner" style="left:787px" role="img" aria-label="Partner badge"><span></span></div>

<!-- footer -->
<svg class="abs zigzag" width="1145" height="7" viewBox="0 0 1145 7" preserveAspectRatio="none">
  <defs><pattern id="teeth" width="20" height="7" patternUnits="userSpaceOnUse"><path d="M0 7 5 0h10l5 7z" fill="#212022"/></pattern></defs>
  <rect width="1145" height="7" fill="url(#teeth)"/>
</svg>
<div class="abs footer"></div>

<div class="abs f-title" style="left:223px;top:886px">SUBSCRIBE OUR NEWSLETTER</div>
<div class="abs news-input">ENTHER YOUR EMAIL</div>
<div class="abs news-btn">SUBSCRIBE</div>

<svg class="abs" style="left:467px;top:885px" width="36" height="40" viewBox="0 0 36 40">
  <g fill="none" stroke="#f04a4f" stroke-width="1.6">
    <path d="M17 2v37"/><path d="M6 6h22v8H6l-4-4z"/><path d="M12 18h18l4 4-4 4H12z"/>
  </g>
</svg>
<div class="abs areas">OUR SERVICING<br>AREAS</div>

<svg class="abs" style="left:728px;top:888px" width="35" height="35" viewBox="0 0 35 35">
  <circle cx="17.5" cy="17.5" r="15" fill="none" stroke="#f04a4f" stroke-width="3"/>
  <path d="M17.5 9v9h-6" fill="none" stroke="#f04a4f" stroke-width="2.6"/>
</svg>
<div class="abs hours"><div class="label">24 HOURS SERVICE AVAILABLE!</div><div class="num">1111 1111</div></div>

<div class="abs f-divider"></div>

<div class="abs f-col" style="left:224px">
  <h3>Browse Repair Locations</h3>
  <div style="display:flex;gap:37px">
    <ul><li>Arizona</li><li>Colorado</li><li>Florida</li><li>Georgia</li><li>Idaho</li><li>Illinois</li><li>Indiana</li><li>Kansas</li><li>Louisiana</li><li>Maryland</li></ul>
    <ul><li>Michigan</li><li>Nevada</li><li>North Carolina</li><li>Ohio</li><li>Oklahoma</li><li>Oregon</li><li>Pennsylvania</li><li>Texas</li><li>Utah</li><li>Washington</li></ul>
  </div>
</div>
<div class="abs f-col" style="left:434px">
  <h3>Collision Repair</h3>
  <ul><li>Online Collision Estimate</li><li>Schedule Appointment</li><li>Auto Body Repair</li><li>Hail Damage Repair</li><li>Paintless Dent Repair</li><li>Financing Your Repair</li></ul>
</div>
<div class="abs f-col" style="left:600px">
  <h3>Why Choose TrueLane?</h3>
  <ul><li>TrueLane for Auto Glass</li><li>TrueLane for Collision Repair</li><li>TrueLane Claims / Deductibles</li><li>TrueLane Collision Gives Back</li></ul>
</div>
<div class="abs f-col" style="left:784px">
  <h3>Employment</h3>
</div>

<div class="abs bottom"></div>
<div class="abs copy">Copyright 2016 | TrueLane Collision Repair - All rights reserved</div>
<div class="abs cards" role="img" aria-label="Accepted payment cards"><span></span><span></span><span></span><span></span></div>
<div class="abs socials" role="img" aria-label="Social media links"><span></span><span></span><span></span><span></span><span></span></div>

</body>
</html>
```